I want both print and ebook covers

book title is "The Classroom MEETING HANDBOOK: Fresh Paths to Partner With Families For Student Growth. I want a dark Teal or Navy Background. Yellow and white letters. Distorted Picture of one teacher, two parents and one child around a table or desk. But no Martians! My name should include "Award Winning Author"

Target Market(s)

teachers and other educators--principals, school psychologists, speech therapists, etc.

Industry/Entity Type

schools

Font styles to use
Other font styles liked:
• I just need to see how it looks

Colors
0054AA
0677BA
7BADD7
CADEEF
E8F1F8
0094D4
00A9DD
6FCCEA
C7EBF8
E9F6FB
FFC000
F8CF3A
FAE287
FDF2CF
FEFAEE

Requirements
Must have
• Title top third of page big enough to be read when reduced greatly in size. Contrast so that it "pops'.
Nice to have
• Teacher, two parents and one child around a table/desk. My name should include 'Award winning author'

```html
<!DOCTYPE html>
<html lang="en">
<head>
<meta charset="utf-8">
<title>The Classroom Meeting Handbook — Cover</title>
<link href="https://fonts.googleapis.com/css2?family=Arimo:wght@400;700&display=swap" rel="stylesheet">
<style>
  :root {
    --backdrop: #e8e8e8;
    --cover-navy: #1d2766;
    --band-navy: #121a4d;
    --amber: #ffc000;
    --soft-yellow: #fae287;
    --white: #ffffff;
    --rule: #f8cf3a;
  }
  html, body {
    margin: 0;
    padding: 0;
    width: 1200px;
    height: 1200px;
    overflow: hidden;
    background: var(--backdrop);
  }
  .book-cover {
    position: absolute;
    left: 241px;
    top: 61px;
    width: 717px;
    height: 1077px;
    background: var(--cover-navy);
    overflow: hidden;
    font-family: "Arimo", Arial, sans-serif;
  }
  .cover-title {
    position: absolute;
    left: 0;
    top: 0;
    width: 717px;
    height: 500px;
  }
  .cover-title text {
    font-family: "Arimo", Arial, sans-serif;
    font-weight: 700;
  }
  .title-white { fill: var(--white); }
  .title-amber { fill: var(--amber); }
  .title-rule { stroke: var(--rule); stroke-width: 3; }
  .cover-subtitle {
    position: absolute;
    left: 0;
    top: 500px;
    width: 100%;
    margin: 0;
    text-align: center;
    color: var(--soft-yellow);
    font-family: "Arimo", Arial, sans-serif;
    font-weight: 700;
    font-size: 30px;
    line-height: 40px;
  }
  .cover-art {
    position: absolute;
    left: 98px;
    top: 610px;
    width: 520px;
    height: 350px;
  }
  .author-band {
    position: absolute;
    left: 0;
    bottom: 0;
    width: 100%;
    height: 82px;
    background: var(--band-navy);
    display: flex;
    align-items: center;
    justify-content: center;
  }
  .author-name {
    margin: 0;
    color: var(--white);
    font-family: "Arimo", Arial, sans-serif;
    font-weight: 700;
    font-size: 38px;
    letter-spacing: 0.5px;
  }
</style>
</head>
<body>
  <main class="book-cover">
    <svg class="cover-title" viewBox="0 0 717 500" role="heading" aria-level="1" aria-label="The Classroom Meeting Handbook">
      <line class="title-rule" x1="88" y1="81" x2="261" y2="81"/>
      <line class="title-rule" x1="456" y1="81" x2="628" y2="81"/>
      <text class="title-white" x="358.5" y="107" font-size="74" text-anchor="middle">THE</text>
      <text class="title-white" x="36" y="209" font-size="121" textLength="646" lengthAdjust="spacingAndGlyphs">CLASSROOM</text>
      <text class="title-amber" x="36" y="337" font-size="160" textLength="646" lengthAdjust="spacingAndGlyphs">MEETING</text>
      <text class="title-white" x="36" y="465" font-size="140" textLength="646" lengthAdjust="spacingAndGlyphs">HANDBOOK</text>
    </svg>

    <p class="cover-subtitle">Fresh Paths to Partner With Families<br>For Student Growth</p>

    <svg class="cover-art" viewBox="0 0 520 350" role="img" aria-label="Illustration of a teacher, two parents and a child meeting around a classroom table">
      <defs>
        <linearGradient id="artTone" x1="0" y1="0" x2="0" y2="1">
          <stop offset="0" stop-color="#c7ebf8"/>
          <stop offset="1" stop-color="#7badd7"/>
        </linearGradient>
      </defs>
      <path d="M75 50 C145 15 220 38 280 34 C355 27 440 25 480 93 C518 152 505 220 480 270 C445 333 352 346 260 342 C168 338 80 338 46 279 C17 224 21 93 75 50 Z" fill="url(#artTone)"/>
    </svg>

    <footer class="author-band">
      <p class="author-name">AWARD WINNING AUTHOR</p>
    </footer>
  </main>
</body>
</html>
```